Website Redesign Project

Bright Harbour Consulting provides project management and project controls consultancy services to companies in many industry sectors, within Australia and overseas. My company has been developing a business brand through forging strong business relationships within industry. We provide innovative tools, concepts and solutions to management teams to assist them in better plan and managing there project portfolios.
SECTORS OF INDUSTRY WE SERVICE
★Oil & Gas
★Minerals & Metals
★Petrochemical
★Manufacturing
★Building & Construction
★Telecommunications
★Rail
★Civil
OLD WEBSITE
My old website www.brightharbourconsulting.com.au needs a complete overhaul in terms of how the web pages look and feel. I am trying to get away from the grey, washed out look as it is uninviting and dull. My clients commented that my webpage does not reflect who I am as a company or my core values. Think total redesign
DESIGN
I would like a webpage design that is modern and has a corporate image. It must be elegant, classy, and have an overall glossy appearance. I want something exciting that creates some excellent feedback from clients. It needs to have a savvy appearance and an attitude of a market leader. A generic website template cannot be used as I provide a unique service to clients. I do not need a website design that looks like my compeditors, I want something that stands out in the crowd and effectivly markets my bussinesses brand. I want my website to represent quality, so only high resolution images that are clear, sharp and in focus can be used. With this design, throw your standard webpage design concepts out the window, as I want something fresh, innovative, exciting and inviting. The overall design should appear uncluttered as all content needs to be there for a reason, so think functional.
It must be professional and of the highest calibre as my clients expect nothing less. I provide clients with innovative tools, concepts and solutions, so the design needs to be edgy and creative to align with my company’s core business services. The new design must promote the company’s brand and us as a market leader. It must communicate that we service many industry sectors and reflect our company’s creativity, vision, energy and drive.
WEBPAGE WRITTEN CONTENT
I am happy with the written content on each page within my old website. You may arrange the text how you see fit within the new design. On the main page of my old website the text is under scored, I am not a big fan of this. I currently do not like the format the text is in, I am looking for a formatt that is easy to read, looks flattering and pleasing to the eye.
MAIN PAGE DESIGN
The main page design needs to focus on my company as a brand, it must promote that I service many industry sectors. My old webpage had me pigeon holed as only providing services to oil and gas. This is incorrect as I service oil & gas, metals and minerals, Petrochemical, Manufacturing, Building & Construction, Telecommunications, Rail and civil.
WEBPAGE COLUR PREFERENCE
Prefer a white background with plenty of colour
TESTIMONIAL TAB
The testimonial tab on the task bar can be removed as it is no longer required.
FINISHED PRODUCT
The finished product will be uploaded by you to a nominated web hosting account. I will need a copy of all files associated with the design. A copy of the finished product will also be provided in formats that can me imported to Xara Pro Designer as I will update my website in 6 months or so using this tool.
Updates
I have updated the design brief after recieving feedback from several designers
Thanks
Hi All
I have just launched another project called "bright harbour consulting business card redesign project", you are all welcome to join this project.
Thanks
Target Market(s)
★Oil and Gas
★Mining and Resources
★Building and infrastructure
★Petrochemical
★Civil and roads
★Rail
Industry/Entity Type
Industry
Requirements
Must have
- ★Draw you in
★Hold your attention
★Identify company brand
★Highlight skills experience and expertise
★Be a unique design not generic
Should not have
- ★The webpage design should not be old fashioned
★ The design should not be based off a generic design template
★The webpage should not be cluttered; everything needs to be there for a reason.

```html
<!DOCTYPE html>
<html lang="en">
<head>
<meta charset="utf-8">
<title>Bright Harbour Consulting</title>
<link href="https://fonts.googleapis.com/css2?family=Arimo:wght@400;700&display=swap" rel="stylesheet">
<style>
:root{
  --ink:#000;
  --paper:#fff;
  --panel:#524d4b;
  --strip:#bcb8b8;
  --accent:#e3161f;
  --muted:#2a2a2a;
  --field:#f7f8fd;
}
*{box-sizing:border-box;margin:0;padding:0}
html,body{width:982px;height:1200px;overflow:hidden;background:var(--paper)}
body{position:relative;font-family:"Arimo",Arial,sans-serif;color:var(--ink)}
.abs{position:absolute}

.brand{left:236px;top:74px;display:flex;align-items:center;gap:14px}
.brand-mark{width:58px;height:58px;border-radius:50%;background:var(--accent)}
.brand-name{font-size:28px;font-weight:700;letter-spacing:.3px;color:var(--ink);white-space:nowrap}
.tagline{left:352px;top:137px;font-size:13px;color:var(--muted);white-space:nowrap}
.top-contact{right:43px;top:194px;text-align:right;font-size:12.5px;line-height:14px;white-space:nowrap}

.main-nav{left:0;top:233px;width:982px;height:40px;background:var(--ink);display:flex;justify-content:center;align-items:center;gap:17px;padding-left:26px}
.main-nav span{color:var(--paper);font-size:16px;white-space:nowrap}

.side-box{background:var(--panel);border-radius:15px;overflow:hidden;color:var(--paper)}
.side-box h2{background:var(--ink);font-weight:400;font-size:22px;padding:22px 0 0 31px;height:52px}
.side-box ul{list-style:none;padding:3px 0 0 31px}
.side-box li{font-size:16px;line-height:28.6px;white-space:nowrap}
.sectors{left:77px;top:298px;width:219px;height:455px}
.services{left:77px;top:800px;width:214px;height:246px}
.services h2{height:49px;padding-top:18px}
.login-label{left:91px;top:615px;font-size:12.5px;color:var(--paper)}
.field{left:90px;width:193px;height:27px;background:var(--field);font-size:10.5px;display:flex;align-items:center;justify-content:center}

.welcome{left:346px;top:298px;width:566px}
.welcome h1{font-weight:400;font-size:15.8px;margin-bottom:19px}
.welcome p{font-size:15.8px;line-height:19.4px}

.hero{left:343px;top:517px;width:557px;height:255px;border-radius:12px;
  background:radial-gradient(ellipse 38% 30% at 52% 62%,#ffd27a 0%,#f59b2b 30%,rgba(245,155,43,0) 75%),
  linear-gradient(180deg,#16263a 0%,#2e4560 38%,#a9672a 60%,#6e3f1a 75%,#1a1410 100%)}
.caption{left:348px;top:777px;font-size:16px;white-space:nowrap}
.caption small{font-size:14px;margin-left:14px}

.strip{left:337px;top:809px;width:572px;height:161px;background:var(--strip)}
.thumb{top:816px;width:182px;height:123px}
.thumb-oil{left:343px;background:radial-gradient(ellipse 35% 25% at 50% 68%,#ffcf70,rgba(255,160,50,0) 70%),linear-gradient(180deg,#15263a,#34506a 45%,#b0702c 66%,#1e1610)}
.thumb-min{left:532px;background:radial-gradient(circle at 45% 60%,#c9a0c4 0%,#6a5a8a 35%,#2b2a3a 75%)}
.thumb-pet{left:721px;background:linear-gradient(180deg,#e9eef3 0%,#c4ccd4 50%,#8fa3b4 62%,#6f9a45 100%)}
.thumb-label{top:943px;font-size:16px;white-space:nowrap}
.arrow{top:852px}

.blurb{top:986px;width:182px;font-size:8.6px;line-height:10.5px}
.more{top:1054px;font-size:8.6px;color:var(--accent)}

.footer{left:0;top:1078px;width:982px;height:122px;background:var(--panel);color:var(--paper);text-align:center}
.socials{display:flex;justify-content:center;gap:20px;margin:11px 0 0 -18px}
.socials span{width:28px;height:28px;border-radius:50%;background:var(--accent);border:1px solid #2a0000}
.foot-nav{display:flex;justify-content:center;gap:14px;margin-top:13px;font-size:13.5px}
.copyright{font-size:10.5px;margin-top:8px}
.foot-contact{font-size:13px;margin-top:5px;white-space:nowrap}
.foot-contact span{margin:0 8px}
</style>
</head>
<body>
<header>
  <div class="abs brand"><span class="brand-mark"></span><span class="brand-name">BRIGHT HARBOUR CONSULTING</span></div>
  <div class="abs tagline">Providing Effective Project Controls and Management Solutions</div>
  <div class="abs top-contact">Tel: 0400 555 218<br>Email: jordanreeve@ brightharbour consulting .com.au</div>
  <nav class="abs main-nav">
    <span>HOME</span><span>ABOUT US</span><span>EXPERTISE</span><span>KNOWLEDGE</span><span>EXPERIENCE</span><span>PROJECTS</span><span>FOCUS</span><span>CONTACT US</span>
  </nav>
</header>

<aside class="abs side-box sectors">
  <h2>Sectors</h2>
  <ul>
    <li>Oil &amp; Gas</li><li>Minerals &amp; Metals</li><li>Petrochemical</li><li>Manufacturing</li><li>Building &amp; Construction</li><li>Telecommunications</li><li>Rail</li><li>Civil</li>
  </ul>
</aside>
<div class="abs login-label">LOG IN / REGISTER NOW</div>
<div class="abs field" style="top:638px">EMAIL ADDRESS</div>
<div class="abs field" style="top:693px">PASSWORD</div>

<aside class="abs side-box services">
  <h2>Services</h2>
  <ul>
    <li>Assisting Clients</li><li>Advice &amp; Solutions</li><li>Benefits</li><li>Values</li><li>Others</li>
  </ul>
</aside>

<main>
  <section class="abs welcome">
    <h1>WELCOME TO BRIGHT HARBOUR CONSULTING</h1>
    <p>I provide services to companies in the mining and oil and gas sector to enabling them to plan and manage their construction projects more effectively. This is achieved by evaluating the businesses practices and them implementing different tools and solutions.<br>My clients are then able to plan and deliver their projects, on time and within their budgets. I am able to provide services to both large and small scale businesses within Australian and Overseas. I offer my clients value by providing, exceptional skills and expertise at a competitive market rate.</p>
  </section>

  <div class="abs hero" role="img" aria-label="Photo of an oil and gas refinery at dusk with pipelines and a glowing sunset"></div>
  <div class="abs caption">Oil &amp; Gas <small>(The enlarged picture above appears once you click the picture below)</small></div>

  <div class="abs strip"></div>
  <svg class="abs arrow" style="left:313px" width="20" height="38" viewBox="0 0 20 38"><polyline points="17,2 2,19 17,36" fill="none" stroke="#000" stroke-width="1.3"/></svg>
  <svg class="abs arrow" style="left:915px" width="20" height="38" viewBox="0 0 20 38"><polyline points="3,2 18,19 3,36" fill="none" stroke="#000" stroke-width="1.3"/></svg>
  <div class="abs thumb thumb-oil" role="img" aria-label="Photo of a refinery lit at sunset"></div>
  <div class="abs thumb thumb-min" role="img" aria-label="Close-up photo of a shimmering mineral ore"></div>
  <div class="abs thumb thumb-pet" role="img" aria-label="Photo of petrochemical tanks and pipelines on grass"></div>
  <div class="abs thumb-label" style="left:345px;font-size:12.5px;top:947px">Oil &amp; Gas</div>
  <div class="abs thumb-label" style="left:530px">Minerals &amp; Metals</div>
  <div class="abs thumb-label" style="left:721px">Petrochemicals</div>

  <p class="abs blurb" style="left:342px">Planning and controls support for upstream and downstream oil and gas projects, from early scheduling through to cost reporting, change control and final handover to operations teams.</p>
  <p class="abs blurb" style="left:536px">Practical project controls for mine and processing plant builds, helping owners track progress, forecast costs and keep large capital works on schedule across remote and demanding sites.</p>
  <p class="abs blurb" style="left:729px">Scheduling, estimating and reporting tools for petrochemical plant upgrades and shutdowns, giving management teams clear visibility of risk, budget and progress at every stage of delivery.</p>
  <span class="abs more" style="left:471px">READ MORE</span>
  <span class="abs more" style="left:663px">READ MORE</span>
  <span class="abs more" style="left:851px">READ MORE</span>
</main>

<footer class="abs footer">
  <div class="socials"><span></span><span></span><span></span><span></span></div>
  <div class="foot-nav"><span>HOME</span><span>ABOUT US</span><span>EXPERTISE</span><span>KNOWLEDGE</span><span>EXPERIENCE</span><span>PROJECTS</span><span>FOCUS</span><span>CONTACT US</span></div>
  <div class="copyright">©COPYRIGHT BY 2013 BRIGHT HARBOUR CONSULTING. ALL RIGHTS RESERVED</div>
  <div class="foot-contact"><span>Tel: 0400 555 218</span><span>Email: jordanreeve@ brightharbour consulting .com.au</span><span>Website: www.brightharbourconsulting.com.au</span></div>
</footer>
</body>
</html>
```